Coral Marriage Counsel Partners Billboard

We are looking for a billboard design for a Florida divorce law firm. We are unique in the legal field for offering flat fee pricing. Other law firms are expensive, charging hourly rates. We have A LOT of lawyers advertising for personal injury, so we are looking for something fun that will catch the attention and drive home the message that we are an affordable firm to hire for their divorce because we charge a fixed fee. We want people to be directed to steadyratesplit.example

Target Market(s)

Individual seeking a fast and affordable divorce at a fixed fee instead of hourly

Industry/Entity Type

Legal

Requirements
Must have
• Name of firm, logo, steadyratesplit.example, and in small font: Main Office Jacksonville
Should not have
• Promises. Price

```html
<!DOCTYPE html>
<html lang="en">
<head>
<meta charset="utf-8">
<title>Coral Marriage Counsel Partners Billboard</title>
<link rel="stylesheet" href="https://fonts.googleapis.com/css2?family=Playfair+Display:wght@400;700;900&display=swap">
<style>
  :root {
    --navy: #17355a;
    --navy-deep: #10284a;
    --gold: #c99a1e;
    --gold-deep: #a97d12;
    --white: #ffffff;
    --stage: #4b4b4b;
    --ink-grey: #555555;
    --serif: "Playfair Display", Georgia, serif;
  }
  * { margin: 0; padding: 0; box-sizing: border-box; }
  html, body { width: 900px; height: 1200px; overflow: hidden; }
  body { background: var(--stage); font-family: var(--serif); font-variant-numeric: lining-nums; }

  .billboard {
    position: absolute; left: 20px; top: 457px;
    width: 860px; height: 286px;
    background: var(--white); overflow: hidden;
  }
  .billboard__bands { position: absolute; inset: 0; }

  .photo-backdrop, .attorney-photo { position: absolute; }
  .attorney-photo {
    left: 535px; top: 36px; width: 150px; height: 250px;
    background: linear-gradient(180deg, #3a3d45 0%, #1d2028 60%, #15171d 100%);
    border-radius: 60px 60px 0 0;
  }
  .photo-backdrop--gavel {
    left: 360px; top: 130px; width: 150px; height: 156px;
    background: linear-gradient(160deg, rgba(90,60,10,0), rgba(90,60,10,.35));
  }
  .photo-backdrop--scales {
    left: 0; top: 150px; width: 140px; height: 105px;
    background: linear-gradient(180deg, rgba(255,255,255,0), rgba(255,255,255,.08));
  }

  .headline { position: absolute; left: 46px; top: 34px; width: 320px; text-align: center; color: var(--white); }
  .headline__lead { font-size: 22px; font-weight: 400; line-height: 1.1; }
  .headline__divorce { font-size: 48px; font-weight: 700; color: var(--gold); line-height: 1.05; letter-spacing: 1px; }
  .headline__attorney { font-size: 40px; font-weight: 700; line-height: 1.05; letter-spacing: 1px; }
  .contact { position: absolute; left: 46px; top: 180px; width: 320px; text-align: center; color: var(--white); }
  .contact__prompt { font-size: 15px; }
  .contact__phone { font-size: 27px; font-weight: 400; line-height: 1.15; letter-spacing: .5px; }
  .site-url { position: absolute; left: 0; top: 259px; width: 340px; text-align: center; font-size: 15px; color: var(--navy-deep); }

  .firm-name { position: absolute; left: 398px; top: 28px; width: 150px; text-align: center; color: var(--white); }
  .firm-name__dot { display: block; width: 30px; height: 30px; margin: 0 auto 6px; border-radius: 50%; background: var(--white); }
  .firm-name__text { font-size: 12px; font-weight: 400; line-height: 1.25; }

  .offer { position: absolute; left: 690px; top: 24px; width: 160px; text-align: center; }
  .offer__dot { display: block; width: 30px; height: 30px; margin: 0 auto 6px; border-radius: 50%; background: var(--navy); }
  .offer__lead { font-size: 16px; font-weight: 700; color: var(--navy); line-height: 1.1; }
  .offer__flat, .offer__fee { font-size: 46px; font-weight: 900; line-height: .95; }
  .offer__flat { color: var(--navy); }
  .offer__fee { color: var(--gold); }
  .offer__pricing { font-size: 19px; font-weight: 700; color: var(--navy); letter-spacing: 1px; }

  .partner { position: absolute; left: 700px; top: 218px; width: 140px; }
  .partner__row { display: flex; align-items: center; gap: 6px; }
  .partner__dot { width: 22px; height: 22px; border-radius: 50%; background: var(--gold); flex: none; }
  .partner__name { font-size: 9px; color: var(--ink-grey); line-height: 1.2; }
  .partner__bar { margin-top: 5px; height: 9px; background: var(--ink-grey); color: var(--white); font-size: 6px; line-height: 9px; text-align: right; padding-right: 4px; }

  .office-note { position: absolute; left: 700px; top: 266px; width: 140px; text-align: center; font-size: 9px; color: var(--navy); letter-spacing: .3px; }
</style>
</head>
<body>
  <main class="billboard">
    <svg class="billboard__bands" width="860" height="286" viewBox="0 0 860 286" aria-hidden="true">
      <polygon points="450,0 672,0 572,286 349,286" fill="var(--gold)"/>
      <polygon points="0,0 450,0 360,255 0,255" fill="var(--navy)"/>
    </svg>

    <div class="photo-backdrop photo-backdrop--scales" role="img" aria-label="Faint photo of scales of justice"></div>
    <div class="photo-backdrop photo-backdrop--gavel" role="img" aria-label="Faint photo of a judge's gavel"></div>
    <div class="attorney-photo" role="img" aria-label="Photo of an attorney in a dark suit and gold tie"></div>

    <div class="headline">
      <p class="headline__lead">Are You In Need Of A</p>
      <p class="headline__divorce">DIVORCE</p>
      <p class="headline__attorney">ATTORNEY?</p>
    </div>
    <div class="contact">
      <p class="contact__prompt">call us today</p>
      <p class="contact__phone">855-555-0143</p>
    </div>
    <p class="site-url">www.steadyratesplit.example</p>

    <div class="firm-name">
      <span class="firm-name__dot"></span>
      <p class="firm-name__text">Coral Marriage<br>Counsel Partners</p>
    </div>

    <div class="offer">
      <span class="offer__dot"></span>
      <p class="offer__lead">we are offering</p>
      <p class="offer__flat">FLAT</p>
      <p class="offer__fee">FEE</p>
      <p class="offer__pricing">PRICING</p>
    </div>

    <div class="partner">
      <div class="partner__row">
        <span class="partner__dot"></span>
        <p class="partner__name">Reed &amp; Reed<br>Divorce Attorneys</p>
      </div>
      <p class="partner__bar">reedandreed.example</p>
    </div>

    <p class="office-note">Main Office Jacksonville</p>
  </main>
</body>
</html>
```